Business Card Design Project

Business Card
We are rebranding with a new logo
Industry/Entity Type
Business
Contact Information for Business Card
Dennis Marlow +61 427581962 dennis@qovo.com.au P.O. Box 872 Kelvindale QLD 4309
Requirements
Must have
- Logo

```html
<!DOCTYPE html>
<html lang="en">
<head>
<meta charset="utf-8">
<title>Qovo International – Business Card</title>
<link rel="stylesheet" href="https://fonts.googleapis.com/css2?family=Mulish:wght@400;700;800&display=swap">
<style>
  :root {
    --page-bg: #e4e5e7;
    --card-top: #ffffff;
    --card-bottom: #e9eaec;
    --navy: #0b4566;
    --ocean: #1a86b5;
    --sky: #2a9fd0;
    --orange: #e0701f;
    --ink: #16222b;
    --light-text: #e6f1f7;
  }
  * { margin: 0; padding: 0; box-sizing: border-box; }
  html, body {
    width: 1200px;
    height: 965px;
    overflow: hidden;
    background: var(--page-bg);
    font-family: "Mulish", sans-serif;
  }
  .business-card {
    position: absolute;
    left: 60px;
    top: 175px;
    width: 1080px;
    height: 614px;
    border-radius: 40px;
    overflow: hidden;
    background: linear-gradient(180deg, var(--card-top) 0%, var(--card-bottom) 70%);
    box-shadow: 0 10px 30px rgba(0, 0, 0, 0.18);
  }
  .card-waves {
    position: absolute;
    inset: 0;
    width: 100%;
    height: 100%;
  }
  .brand {
    position: absolute;
    right: 40px;
    top: 160px;
    text-align: right;
    color: var(--navy);
    font-weight: 800;
    line-height: 1;
  }
  .brand-name {
    display: block;
    font-size: 112px;
    letter-spacing: 2px;
  }
  .brand-tagline {
    display: block;
    margin-top: 22px;
    font-size: 35px;
    letter-spacing: 5px;
  }
  .holder-name {
    position: absolute;
    left: 53px;
    top: 395px;
    font-size: 31px;
    font-weight: 800;
    color: var(--orange);
  }
  .contact-list {
    position: absolute;
    left: 50px;
    top: 493px;
    list-style: none;
  }
  .contact-list li {
    display: flex;
    align-items: center;
    height: 31px;
    font-size: 24px;
    color: var(--light-text);
  }
  .contact-list svg {
    width: 22px;
    height: 22px;
    margin-right: 15px;
    flex: none;
  }
  .postal-address {
    position: absolute;
    left: 396px;
    top: 524px;
    font-style: normal;
    font-size: 24px;
    line-height: 31px;
    color: var(--light-text);
  }
</style>
</head>
<body>
  <div class="business-card">
    <svg class="card-waves" viewBox="0 0 980 557" preserveAspectRatio="none" aria-hidden="true">
      <defs>
        <linearGradient id="blueBody" x1="0" y1="0" x2="1" y2="0.3">
          <stop offset="0" stop-color="#0b4566"/>
          <stop offset="0.55" stop-color="#12648f"/>
          <stop offset="1" stop-color="#1a8cbd"/>
        </linearGradient>
        <linearGradient id="skyBand" x1="0" y1="0" x2="1" y2="0">
          <stop offset="0" stop-color="#1a86b5" stop-opacity="0"/>
          <stop offset="0.4" stop-color="#1a86b5"/>
          <stop offset="1" stop-color="#2a9fd0"/>
        </linearGradient>
      </defs>
      <!-- main blue body -->
      <path d="M0,318 C70,262 200,248 330,288 C460,328 560,385 680,410 C800,432 900,425 980,405 L980,557 L0,557 Z" fill="url(#blueBody)"/>
      <!-- thin orange edge -->
      <path d="M0,318 C70,262 200,248 330,288 C460,328 560,385 680,410 C800,432 900,425 980,405 L980,448 C900,462 800,462 680,440 C600,426 540,400 470,370 C420,350 380,330 330,292 C200,254 70,268 0,322 Z" fill="var(--orange)"/>
      <!-- blue beneath orange at right -->
      <path d="M0,322 C70,268 200,254 330,292 C380,330 420,350 470,370 C540,400 600,426 680,440 C800,462 900,462 980,448 L980,557 L0,557 Z" fill="url(#blueBody)"/>
      <!-- dark band under orange -->
      <path d="M560,410 C620,440 680,458 760,466 C850,474 920,470 980,462 L980,478 C900,488 820,488 740,478 C670,468 610,445 560,410 Z" fill="#0b4566" opacity="0.6"/>
      <!-- white separator and sky band on the right -->
      <path d="M600,388 C680,410 760,418 840,410 C900,404 945,392 980,378 L980,408 C930,418 880,424 820,422 C740,420 670,406 600,388 Z" fill="#ffffff"/>
      <path d="M600,386 C680,406 760,412 840,404 C900,398 945,388 980,372 L980,402 C930,414 880,420 820,418 C740,416 670,404 600,386 Z" fill="url(#skyBand)"/>
      <!-- highlight on left crest -->
      <path d="M0,336 C80,282 200,270 320,300 C200,282 90,300 0,360 Z" fill="#2a9fd0" opacity="0.35"/>
    </svg>

    <div class="brand">
      <span class="brand-name">QOVO</span>
      <span class="brand-tagline">INTERNATIONAL</span>
    </div>

    <p class="holder-name">Dennis Marlow</p>

    <ul class="contact-list">
      <li>
        <svg viewBox="0 0 24 24" aria-hidden="true"><path d="M6.6 10.8c1.4 2.8 3.8 5.1 6.6 6.6l2.2-2.2c.3-.3.7-.4 1-.2 1.1.4 2.3.6 3.6.6.6 0 1 .4 1 1V20c0 .6-.4 1-1 1C10.6 21 3 13.4 3 4c0-.6.4-1 1-1h3.5c.6 0 1 .4 1 1 0 1.3.2 2.5.6 3.6.1.3 0 .7-.2 1z" fill="var(--orange)"/></svg>
        +61 427581962
      </li>
      <li>
        <svg viewBox="0 0 24 24" aria-hidden="true"><rect x="2" y="5" width="20" height="14" rx="1.5" fill="var(--orange)"/><path d="M2.5 6 12 13l9.5-7" fill="none" stroke="#0b4566" stroke-width="1.6"/></svg>
        dennis@qovo.com.au
      </li>
      <li>
        <svg viewBox="0 0 24 24" aria-hidden="true"><g fill="none" stroke="var(--orange)" stroke-width="1.8"><circle cx="12" cy="12" r="9.5"/><ellipse cx="12" cy="12" rx="4.2" ry="9.5"/><path d="M2.5 12h19M4 7h16M4 17h16"/></g></svg>
        www.qovo.com.au
      </li>
    </ul>

    <address class="postal-address">P.O. Box 872 Kelvindale<br>QLD 4309</address>
  </div>
</body>
</html>
```